Web site for mobile& web developers

We need a web site design for our company, Tamblin Reef Works Pty Ltd.

We are a Sydney based, software development company specialising in mobile platforms and web applications. We are a small, dynamic team with a few awesome products we want to get out to the world.

We would prefer a clean, professional layout that incorporates the company logo and branding; we do have a youthful, start-up edge which we would like to express.

We technical people with damn good products, so your design has to make us look good to non-technical people too!

Target Market(s)

B2B, Enterprise technology, Project Managers, Marketing, Other developers

Industry/Entity Type

It Company

Requirements
Must have
• Required pages:
- home page - this must allow us to feature our software (mobile & web) on the home page
- a standard content page (for things like "about us", "our team", etc)
- contact us (including HTML form with error state)
- mobile (iOS and Android) product page - allow for screen shots, features, requirements, customer list
- web product page - allow for screen shots, features, requirements, customer list

You must incorporate our logo and branding into the theme.
Should not have
• HTML/CSS carve is not required. We only required layered PNGs or PSDs.

```html
<!DOCTYPE html>
<html lang="en">
<head>
<meta charset="utf-8">
<title>Tamblin Reef Works — Home</title>
<link rel="stylesheet" href="https://fonts.googleapis.com/css2?family=Arimo:ital,wght@0,400;0,700;1,400&family=PT+Sans:wght@400&family=Source+Sans+3:wght@400&display=swap">
<style>
:root{
  --page:#e9e9e9;
  --panel:#ffffff;
  --ink:#222222;
  --body:#444444;
  --muted:#888888;
  --rule:#cfcfcf;
  --nav-top:#4a4a4a;
  --nav-bottom:#222222;
  --nav-active:#151515;
  --brand-blue:#2a8fc0;
  --drop-blue:#1b97c9;
  --link-red:#c2220e;
  --hiring:#5bb8e6;
  --footer:#050505;
  --footer-text:#3a3a3a;
  --footer-nav:#8a8a8a;
}
*{box-sizing:border-box;margin:0;padding:0}
html,body{width:885px;height:1200px;overflow:hidden}
body{position:relative;background:var(--page);font-family:"Arimo",Arial,sans-serif;color:var(--body)}
.abs{position:absolute}
a{color:inherit;text-decoration:none}

/* header */
.brand-mark{left:186px;top:6px;width:54px;height:54px;border-radius:50%;background:#3f8fd0}
.brand-name{left:68px;top:72px;font-size:16px;letter-spacing:1px;color:#4b4b4b;font-weight:700;white-space:nowrap}
.brand-divider{left:288px;top:68px;width:1px;height:26px;background:#bbb}
.tagline{left:306px;top:73px;font-family:"PT Sans",sans-serif;font-size:14.5px;color:var(--brand-blue);white-space:nowrap}
.contact{left:680px;top:41px;font-size:9.5px;line-height:19px;color:#333;white-space:nowrap}

/* nav */
.nav{left:52px;top:99px;width:760px;height:39px;background:linear-gradient(var(--nav-top),var(--nav-bottom))}
.nav-item{top:13px;font-size:12.5px;color:#f2f2f2}
.nav-active{left:9px;top:7px;width:57px;height:25px;background:var(--nav-active);border:1px solid #000}
.search{left:559px;top:7px;width:162px;height:24px;background:#fff;font-size:9.5px;color:#555;padding:7px 8px}
.search-btn{left:721px;top:7px;width:27px;height:24px;background:#2c2c2c}

.panel{left:52px;top:138px;width:760px;height:585px;background:var(--panel)}

/* slider */
.slider{left:59px;top:147px;width:744px;height:311px;background:radial-gradient(ellipse at 55% 55%,#6fb6df 0%,#2c6f9c 35%,#0f3552 75%,#07192a 100%)}
.slide-caption{left:106px;top:296px;width:650px;height:80px;background:rgba(40,50,60,.72);border-radius:6px;color:#fff;font-family:"Source Sans 3",sans-serif;font-size:18.5px;letter-spacing:-.4px;padding:26px 0 0 23px;white-space:nowrap}
.slide-caption b{font-weight:400;font-size:21px}
.slide-arrow{top:320px;width:30px;height:30px;border-radius:50%;background:rgba(255,255,255,.55)}
.slide-dots{left:369px;top:440px;width:121px;height:18px;background:#111}
.slide-dots span{position:absolute;top:5px;width:7px;height:7px;border-radius:50%;background:#555}

/* dropdown */
.dropdown{left:330px;top:140px;width:141px}
.dropdown div{height:24.5px;background:var(--drop-blue);border:1px solid #e6f4fb;border-top:none;color:#fff;font-size:9.5px;padding:7px 0 0 14px}

/* quote */
.quote{left:90px;top:477px;width:680px;font-style:italic;font-size:14px;line-height:17px;color:#9a9a9a}
.quote-by{left:667px;top:511px;font-size:9.5px;font-style:italic;color:var(--brand-blue)}
.quote-shadow{left:60px;top:530px;width:745px;height:12px;background:linear-gradient(rgba(0,0,0,.06),rgba(0,0,0,0))}

/* features */
.feature-title{top:573px;font-size:11px;font-weight:700;color:var(--ink)}
.feature-art{border-radius:6px}
.feature-text{top:604px;width:154px;font-size:8.7px;line-height:15.5px;color:#333}
.more{font-size:9px;color:var(--link-red);white-space:nowrap}

/* who we are */
.section-title{left:86px;top:764px;font-size:13.5px;color:#222}
.section-rule{left:74px;top:784px;width:452px;height:1px;background:var(--rule)}
.who-frame{left:74px;top:796px;width:184px;height:84px;border:1px solid #c8c8c8;background:#fff;padding:3px}
.who-art{width:100%;height:100%;background:linear-gradient(100deg,#2d6fb8,#6fb1e4 55%,#d8eaf6)}
.who-text{left:266px;top:794px;width:266px;font-size:8.6px;line-height:15.7px;color:#333}

/* news */
.news-head{left:584px;top:746px;font-size:11px;font-weight:700;color:#111}
.news-sub,.news-body{font-size:8.8px;color:#555;white-space:nowrap}
.news-rule{left:584px;width:210px;height:1px;background:var(--rule)}
.news-date{font-size:8.6px;color:var(--brand-blue)}
.news-date b{color:var(--brand-blue)}
.news-title{font-size:8.4px;font-weight:700;color:#111}

/* hiring band */
.hiring-band{left:0;top:942px;width:885px;height:43px;background:#f7f7f7;border-top:1px solid #dedede}
.hiring{left:586px;top:947px;font-family:"Source Sans 3",sans-serif;font-size:26px;letter-spacing:-1.2px;color:var(--hiring);white-space:nowrap}

/* footer */
.footer{left:0;top:985px;width:885px;height:215px;background:var(--footer)}
.footer-mark{left:191px;top:1005px;width:55px;height:55px;border-radius:50%;background:#2f6aa8}
.footer-name{left:73px;top:1071px;font-size:16.5px;font-weight:700;letter-spacing:1px;color:#bdbdbd;white-space:nowrap}
.footer-info{left:73px;top:1104px;font-size:10.5px;line-height:18.5px;color:var(--footer-text)}
.footer-nav{top:1007px;font-size:9.5px;color:var(--footer-nav)}
.footer-rule{height:1px;background:#2a2a2a}
.follow{left:500px;top:1120px;width:118px;height:18px;background:#111;font-size:8px;color:#555;padding:4px 0 0 6px;white-space:nowrap}
.social{top:1118px;width:24px;height:24px;border-radius:3px}
.copyright{left:598px;top:1167px;font-size:8.4px;color:#eee;white-space:nowrap}
</style>
</head>
<body>

<header>
  <div class="abs brand-mark" aria-hidden="true"></div>
  <div class="abs brand-name">TAMBLIN REEF WORKS</div>
  <div class="abs brand-divider"></div>
  <div class="abs tagline">Make good ide@s GREAT Products.</div>
  <div class="abs contact">E-mail:&nbsp; info@tamblinreef.com<br>Office: Sydney, Australia<br>Phone: +61 2 9000 4312</div>
</header>

<div class="abs panel"></div>

<nav class="abs nav">
  <div class="abs nav-active"></div>
  <a class="abs nav-item" style="left:21px">About</a>
  <a class="abs nav-item" style="left:81px">Services</a>
  <a class="abs nav-item" style="left:148px">News</a>
  <a class="abs nav-item" style="left:212px">Contact</a>
  <a class="abs nav-item" style="left:278px">Work with us</a>
  <div class="abs search">Search:</div>
  <div class="abs search-btn">
    <svg width="27" height="24" viewBox="0 0 27 24"><circle cx="12.5" cy="10.5" r="4" fill="none" stroke="#eee" stroke-width="2"/><line x1="15.5" y1="13.5" x2="19" y2="17" stroke="#eee" stroke-width="2.2"/></svg>
  </div>
</nav>

<section>
  <div class="abs slider" role="img" aria-label="Finger touching a glowing grid of translucent blue squares"></div>
  <div class="abs slide-caption"><b>Tamblin Reef</b> are experts at online and mobile software application development</div>
  <div class="abs slide-arrow" style="left:68px"><svg width="30" height="30"><path d="M17 9 L11 15 L17 21" fill="none" stroke="#fff" stroke-width="3"/></svg></div>
  <div class="abs slide-arrow" style="left:763px"><svg width="30" height="30"><path d="M13 9 L19 15 L13 21" fill="none" stroke="#fff" stroke-width="3"/></svg></div>
  <div class="abs slide-dots">
    <span style="left:11px;background:#fff"></span><span style="left:25px"></span><span style="left:39px"></span><span style="left:53px"></span><span style="left:67px"></span><span style="left:81px"></span><span style="left:95px"></span>
  </div>
</section>

<div class="abs dropdown">
  <div style="border-top:1px solid #e6f4fb">Mobile</div>
  <div>Python</div>
  <div>Digital experience</div>
</div>

<div class="abs quote">Break the BAU vs Project cycle with our Digital Portfolio Management. We offer managed services of BAU systems so your team can get on with revenue making working.</div>
<div class="abs quote-by">by: Alex Marlow</div>
<div class="abs quote-shadow"></div>

<section>
  <h3 class="abs feature-title" style="left:79px">Software Development</h3>
  <div class="abs feature-art" style="left:68px;top:601px;width:75px;height:72px;border-radius:50%;background:radial-gradient(circle,#5fa8e6,#1d4fa6 60%,#c9d6ea)" role="img" aria-label="Globe with circular refresh arrows"></div>
  <p class="abs feature-text" style="left:153px">In a connected world where there are plenty of competitors to your site or product that users can go to as an alternative, User Centred Design is</p>
  <a class="abs more" style="left:205px;top:672px">continue reading »</a>

  <h3 class="abs feature-title" style="left:331px">Mobile Platforms</h3>
  <div class="abs feature-art" style="left:310px;top:599px;width:86px;height:90px;background:linear-gradient(135deg,#3a3a3a,#111 60%,#5a7fa8)" role="img" aria-label="Group of smartphones and a tablet"></div>
  <p class="abs feature-text" style="left:409px">In a connected world where there are plenty of competitors to your site or product that users can go to as an alternative, User Centred Design is</p>
  <a class="abs more" style="left:412px;top:668px">continue reading »</a>

  <h3 class="abs feature-title" style="left:581px">Web Applications</h3>
  <div class="abs feature-art" style="left:562px;top:605px;width:80px;height:75px;background:linear-gradient(135deg,#7ab8f0,#2a6fd0)" role="img" aria-label="Blueprint with hammer and ruler"></div>
  <p class="abs feature-text" style="left:655px">In a connected world where there are plenty of competitors to your site or product that users can go to as an alternative, User Centred Design is more important then ever before. A user</p>
  <a class="abs more" style="left:722px;top:688px">continue reading »</a>
</section>

<section>
  <h2 class="abs section-title" style="font-weight:400">Who we are</h2>
  <div class="abs section-rule"></div>
  <div class="abs who-frame"><div class="who-art" role="img" aria-label="Person leaping against abstract blue curves"></div></div>
  <div class="abs who-text">
    <p>We are passionate about quality products. Our core focus is on producing quality user centric products from your ideas. Bleeding edge technologies, high-volume consumer digital products and knowing your audience are our bread and butter. .</p>
    <p style="margin-top:15.7px">We are the leading online and mobile technology BPO in the Asia Pacific region. We have the passion, the talent and the network to make your idea the next big thing.</p>
  </div>
  <a class="abs more" style="left:462px;top:916px">read more »</a>
</section>

<aside>
  <h3 class="abs news-head">NEWS AND EVENTS</h3>
  <p class="abs news-sub" style="left:584px;top:764px">Standing out from the crowd is vital to your success.</p>
  <div class="abs news-rule" style="top:784px"></div>
  <p class="abs news-date" style="left:584px;top:795px">12 Dec 2009 | <b>0 comments</b></p>
  <p class="abs news-title" style="left:584px;top:811px">STANDING OUT FROM THE CROWD</p>
  <p class="abs news-body" style="left:584px;top:826px">Standing out from the crowd is vital to your success.</p>
  <div class="abs news-rule" style="top:846px"></div>
  <p class="abs news-date" style="left:584px;top:857px">18 Dec 2009 | <b>5 comments</b></p>
  <p class="abs news-title" style="left:584px;top:873px">STANDING OUT FROM THE CROWD</p>
  <p class="abs news-body" style="left:584px;top:888px">Standing out from the crowd is vital to your success.</p>
  <a class="abs more" style="left:584px;top:904px;font-size:8.6px">more news »</a>
</aside>

<div class="abs hiring-band"></div>
<div class="abs hiring">We are hiring!</div>

<footer>
  <div class="abs footer"></div>
  <div class="abs footer-mark" aria-hidden="true"></div>
  <div class="abs footer-name">TAMBLIN REEF WORKS</div>
  <div class="abs footer-info">Make good ideas GREAT Products.<br>E-mail: - info@tamblinreef.com<br>Office location: Sydney, Australia<br>Phone: +61 2 9000 4312</div>

  <a class="abs footer-nav" style="left:558px">About</a>
  <a class="abs footer-nav" style="left:606px">Services</a>
  <a class="abs footer-nav" style="left:660px">News</a>
  <a class="abs footer-nav" style="left:711px">Contact</a>
  <a class="abs footer-nav" style="left:764px">Work with us</a>
  <div class="abs footer-rule" style="left:555px;top:1026px;width:265px"></div>
  <div class="abs footer-rule" style="left:374px;top:1104px;width:446px"></div>

  <div class="abs follow">Follow us on social network</div>
  <div class="abs social" style="left:631px;background:#3b5a9a" aria-label="Social link"></div>
  <div class="abs social" style="left:664px;background:#47b4e0" aria-label="Social link"></div>
  <div class="abs social" style="left:697px;background:#2a2a2a" aria-label="Social link"></div>
  <div class="abs social" style="left:731px;background:#1f79b4" aria-label="Social link"></div>
  <div class="abs social" style="left:764px;background:#3c5a78" aria-label="Social link"></div>
  <div class="abs social" style="left:797px;background:#f18a1c" aria-label="Feed link"></div>

  <p class="abs copyright">© Copyright 2012&nbsp; TAMBLINREEF.COM . All Rights Reserved.</p>
</footer>

</body>
</html>
```